Marrowfield Flock Patrol Trade Show Booth Design

I need a design for our tradeshow booth. It will be 7.5'x7.5' and need a print ready pdf file to upload for it. Specifics are here https://www.plakavento.com/signs-posters/pop-up-displays
We are a goose control company that uses highly trained Border Collies. Our logo and web address should be on board. www.marrowfieldflock.com
I've attached a pic of our tablecloth if that helps color scheme.
I'd like some of this information included, whatever fits best.
Our method is the most effective and humane way to control geese. 100% satisfaction guaranteed. Over 20 years experience. Methods are endorsed by the NBRA, The Gentle Keepers League Federal Marsh & Meadow Bureau and OKRI. We offer Nesting Services. Highest Trained Border Collies. Call us for Free Demonstration.
I have photos of our dogs and would like some kind of photo of a stalking border collie. Either one of ours that I can provide or a stock pic off the internet. I'd like some goose images as well. I can provide actual photos if needed. I'll upload the logo's but can add additional animal pics on request. The "shield" logo is our primary, the non shield is secondary and im open to using either one. I also have larger files of logo

```html
<!DOCTYPE html>
<html lang="en">
<head>
<meta charset="utf-8">
<title>Marrowfield Flock Patrol – Booth Panel</title>
<link rel="stylesheet" href="https://fonts.googleapis.com/css2?family=Ubuntu:wght@400;500;700&display=swap">
<style>
  :root {
    --backdrop: #a9a5a6;
    --paper: #ffffff;
    --ink-black: #050505;
    --signal-red: #e5282d;
    --flag-gold: #f7c90f;
    --text-light: #ffffff;
    --text-dark: #151515;
    --photo-warm: #8a6a47;
    --photo-dark: #2b2622;
    --photo-pale: #d9d6d2;
  }
  html, body {
    margin: 0;
    width: 1200px;
    height: 1200px;
    overflow: hidden;
    background: var(--backdrop);
  }
  .booth-panel {
    position: absolute;
    left: 77px;
    top: 77px;
    width: 1045px;
    height: 1045px;
    background: var(--paper);
    box-shadow: 0 4px 10px rgba(0,0,0,0.25);
  }
  .booth-panel svg { display: block; width: 100%; height: 100%; }
  .shield-field { fill: var(--ink-black); }
  .gold-edge { fill: none; stroke: var(--flag-gold); stroke-width: 10; }
  .red-edge { fill: none; stroke: var(--signal-red); stroke-width: 6; stroke-linejoin: miter; }
  .pitch-copy {
    font-family: "Ubuntu", sans-serif;
    font-weight: 400;
    fill: var(--text-light);
    text-anchor: end;
  }
  .pitch-copy.body { font-size: 21.5px; }
  .pitch-copy.emphasis { font-size: 27px; }
  .call-to-action {
    font-family: "Ubuntu", sans-serif;
    font-weight: 700;
    font-size: 36px;
    fill: var(--signal-red);
    text-anchor: end;
  }
  .brand-name {
    font-family: "Ubuntu", sans-serif;
    font-weight: 700;
    font-size: 27px;
    fill: var(--signal-red);
    text-anchor: middle;
  }
  .web-address {
    font-family: "Ubuntu", sans-serif;
    font-weight: 500;
    font-size: 21px;
    fill: var(--text-dark);
    text-anchor: end;
  }
</style>
</head>
<body>
  <main class="booth-panel">
    <svg viewBox="0 0 836 836" xmlns="http://www.w3.org/2000/svg">
      <defs>
        <linearGradient id="collieTones" x1="0" y1="0" x2="1" y2="1">
          <stop offset="0" stop-color="var(--photo-warm)"/>
          <stop offset="0.45" stop-color="var(--photo-pale)"/>
          <stop offset="0.7" stop-color="var(--photo-dark)"/>
          <stop offset="1" stop-color="var(--photo-warm)"/>
        </linearGradient>
      </defs>

      <!-- Border collie photograph area -->
      <path class="collie-photo" role="img" aria-label="Photo of a black border collie resting outdoors, looking to the right"
            fill="url(#collieTones)"
            d="M0,55 L68,45 Q300,62 378,152 L300,480 Q140,640 28,818 L0,818 Z"/>

      <!-- Black shield panel -->
      <path class="shield-field"
            d="M56,0 L836,0 L836,593 L628,738 L298,478 L378,152 Q300,62 68,45 Z"/>

      <!-- Gold and red trims -->
      <path class="gold-edge" d="M68,45 Q300,62 378,152 L300,480"/>
      <path class="red-edge" d="M298,478 L628,738 L836,593"/>
      <path class="red-edge" d="M56,0 L68,45" style="stroke-width:4"/>

      <!-- Sales copy -->
      <text class="pitch-copy body" x="786" y="98">Our method is the most effective</text>
      <text class="pitch-copy body" x="786" y="128">and humane way to control geese.</text>

      <text class="pitch-copy body" x="786" y="195">100% satisfaction guaranteed.</text>
      <text class="pitch-copy emphasis" x="786" y="236">Over 20 years experience.</text>

      <text class="pitch-copy body" x="786" y="296">Methods are endorsed by the</text>
      <text class="pitch-copy body" x="786" y="327">NBRA, The Gentle Keepers League</text>
      <text class="pitch-copy body" x="786" y="358">Federal Marsh &amp; Meadow Bureau and OKRI.</text>

      <text class="pitch-copy body" x="786" y="425">We offer Nesting Services.</text>
      <text class="pitch-copy body" x="786" y="457">Highest Trained Border Collies.</text>

      <text class="call-to-action" x="786" y="542">Call us for FREE</text>
      <text class="call-to-action" x="786" y="594">Demonstration.</text>

      <!-- Brand name -->
      <text class="brand-name" x="326" y="700">Marrowfield</text>
      <text class="brand-name" x="326" y="734">Flock Patrol</text>

      <!-- Web address -->
      <text class="web-address" x="786" y="786">www.marrowfieldflock.com</text>
    </svg>
  </main>
</body>
</html>
```